Marvel Brookworks highend custom homes

We build high end custom homes and timber frames we specialize in rustic hand made designs along with iron and concrete accents to add a modern touch 90% of my homes are buit on lake front properries attached is my logo and slogan as of now and my previous one

Target Market(s)

High end custom homes

Industry/Entity Type

Custom residential construction

Contact Information for Business Card

Been in buissness 8+ years inssured and reliable

Colors
A7469A
B969AE
D3A5CF
EDDBEB
F8F0F9

Requirements
Must have
• Must have slogan and phone number
Should not have
• A combination of rustic yet modern accents

```html
<!DOCTYPE html>
<html lang="en">
<head>
<meta charset="utf-8">
<title>Marvel Brookworks – Business Card</title>
<link href="https://fonts.googleapis.com/css2?family=Montserrat:wght@400;500;700&display=swap" rel="stylesheet">
<style>
  :root {
    --backdrop: #3b3b3b;
    --card: #161616;
    --card-edge: #4d5f4a;
    --sage: #6b8466;
    --ink: #f2f2f2;
    --rule: #5a5a5a;
    --pattern-dark: #1d1d1d;
    --pattern-light: #3a3a3a;
  }
  * { box-sizing: border-box; margin: 0; padding: 0; }
  html, body {
    width: 1200px; height: 801px; overflow: hidden;
    background: var(--backdrop);
    font-family: "Montserrat", sans-serif;
    color: var(--ink);
  }
  .stage {
    position: relative; width: 1200px; height: 801px;
    display: flex; align-items: center; justify-content: center; gap: 50px;
  }
  .card {
    position: relative; width: 525px; height: 300px;
    background: var(--card);
    border-bottom: 2px solid var(--card-edge);
    box-shadow: 0 18px 40px rgba(0,0,0,.45);
    overflow: hidden;
  }
  /* Front */
  .brand {
    position: absolute; top: 34px; right: 36px;
    display: flex; align-items: center; gap: 10px;
  }
  .brand-mark { width: 34px; height: 34px; background: var(--sage); flex: none; }
  .brand-text { text-align: left; }
  .brand-name {
    font-weight: 700; font-size: 22px; letter-spacing: .5px;
    color: var(--sage); text-transform: uppercase; line-height: 1.05;
  }
  .brand-slogan {
    font-size: 8px; letter-spacing: 1.4px; text-transform: uppercase;
    color: var(--ink); margin-top: 5px; white-space: nowrap;
  }
  .divider-main {
    position: absolute; left: 230px; right: 0; top: 128px;
    height: 1px; background: var(--rule);
  }
  .person { position: absolute; left: 34px; top: 168px; }
  .person-name {
    font-weight: 700; font-size: 17px; letter-spacing: 1px;
    color: var(--sage); text-transform: uppercase;
  }
  .person-title { font-size: 13px; margin-top: 2px; }
  .divider-person {
    position: absolute; left: 34px; top: 216px; width: 250px;
    height: 1px; background: var(--rule);
  }
  .contacts {
    position: absolute; left: 34px; top: 228px;
    list-style: none; font-size: 13px; line-height: 19px;
  }
  .contacts li { display: flex; align-items: center; gap: 8px; white-space: nowrap; }
  .contacts svg { width: 10px; height: 10px; fill: var(--sage); flex: none; }
  .address {
    position: absolute; right: 36px; top: 150px;
    text-align: right; font-size: 13.5px; line-height: 19px;
  }
  /* Back */
  .back-pattern {
    position: absolute; inset: 0;
    background: linear-gradient(120deg, var(--pattern-light) 0%, var(--pattern-dark) 55%, #0f0f0f 100%);
  }
  .back-brand {
    position: absolute; left: 310px; top: 150px;
    display: flex; align-items: center; gap: 8px;
    background: var(--card); padding: 6px 10px;
  }
  .back-brand .brand-mark { width: 22px; height: 22px; }
  .back-brand .brand-name { font-size: 15px; }
</style>
</head>
<body>
  <main class="stage">
    <section class="card card-front">
      <div class="brand">
        <span class="brand-mark"></span>
        <div class="brand-text">
          <div class="brand-name">Marvel<br>Brookworks</div>
          <div class="brand-slogan">◦ Lakeside homes, handcrafted ◦</div>
        </div>
      </div>
      <div class="divider-main"></div>
      <div class="person">
        <div class="person-name">Reid Castellan</div>
        <div class="person-title">President</div>
      </div>
      <div class="divider-person"></div>
      <ul class="contacts">
        <li><svg viewBox="0 0 10 10"><path d="M2 0h2l1 3-1.5 1a6 6 0 0 0 2.5 2.5L7 5l3 1v2c0 1-1 2-2 2A8 8 0 0 1 0 2c0-1 1-2 2-2z"/></svg>555-018-3427</li>
        <li><svg viewBox="0 0 10 10"><path d="M0 2h10v6H0z"/></svg>info@marvelbrookworks.com</li>
        <li><svg viewBox="0 0 10 10"><circle cx="5" cy="5" r="5"/></svg>www.marvelbrookworks.com</li>
      </ul>
      <div class="address">1840 Alder Cove Road<br>Lakeview CA 96150</div>
    </section>

    <section class="card card-back">
      <div class="back-pattern" role="img" aria-label="Repeating monogram pattern in glossy black tones"></div>
      <div class="back-brand">
        <span class="brand-mark"></span>
        <span class="brand-name">Marvel Brookworks</span>
      </div>
    </section>
  </main>
</body>
</html>
```